Quarn Corporate Letterhead

- We would like a letterhead using our logo (can be supplied as vector if needed)
- Would like to have the logo on a clear background
- Please send logo design as a separate file
- Letterhead information:
Quarn Energy Inc.
482 W. Brook Ave. Suite 214
Pasadena, CA 91847

Colors
0555a3
3276b5
85abd2
000000
1b1b1b
757575
c7c7c7
e8e8e8

```html
<!DOCTYPE html>
<html lang="en">
<head>
<meta charset="utf-8">
<title>Quarn Corporate Letterhead</title>
<link href="https://fonts.googleapis.com/css2?family=Arimo:wght@400;700&display=swap" rel="stylesheet">
<style>
  :root {
    --blue-deep: #0555a3;
    --blue-mid: #3276b5;
    --blue-soft: #85abd2;
    --ink: #000000;
    --ink-soft: #1b1b1b;
    --grey: #757575;
    --grey-light: #c7c7c7;
    --paper-shade: #e8e8e8;
    --paper: #ffffff;
  }
  html, body {
    margin: 0;
    width: 1200px;
    height: 795px;
    overflow: hidden;
    background: var(--paper-shade);
  }
  .letterhead {
    position: absolute;
    left: 330px;
    top: 16px;
    width: 540px;
    height: 764px;
    background: var(--paper);
    box-shadow: 0 2px 10px rgba(0,0,0,.12);
    font-family: "Arimo", Arial, sans-serif;
    color: var(--ink-soft);
    font-size: 9.5px;
    line-height: 1.3;
  }
  .brand {
    position: absolute;
    left: 52px;
    top: 48px;
    display: flex;
    align-items: center;
    gap: 8px;
    font-size: 30px;
    font-weight: 700;
    color: var(--blue-deep);
    letter-spacing: 1px;
  }
  .brand-dot {
    width: 14px;
    height: 14px;
    border-radius: 50%;
    background: var(--blue-mid);
  }
  .letter-body {
    position: absolute;
    left: 52px;
    top: 150px;
    width: 420px;
  }
  .date { margin: 0 0 14px; }
  .recipient { margin: 0 0 14px; font-weight: 700; }
  .salutation { margin: 0 0 14px; font-weight: 700; }
  .letter-body p.para { margin: 0 0 14px; color: var(--grey); text-align: justify; }
  .closing {
    position: absolute;
    left: 52px;
    top: 520px;
  }
  .closing p { margin: 0; }
  .signature {
    width: 120px;
    height: 26px;
    margin: 6px 0 4px;
    background: linear-gradient(90deg, var(--ink-soft), var(--grey));
    opacity: .85;
    border-radius: 3px;
  }
  .contact {
    position: absolute;
    right: 30px;
    bottom: 58px;
    text-align: right;
    font-size: 9px;
    color: var(--ink);
  }
  .contact p { margin: 0 0 2px; }
  .contact b { font-weight: 700; }
  .edge-lines {
    position: absolute;
    left: 0;
    bottom: 0;
  }
</style>
</head>
<body>
  <article class="letterhead">
    <div class="brand"><span class="brand-dot"></span>Quarn</div>

    <section class="letter-body">
      <p class="date">January 12, 2014</p>
      <p class="recipient">Mr. Alan Price<br>President<br>AA Corporation<br>111 Street Name, Suite#<br>City, State, 12345</p>
      <p class="salutation">Dear Mr. Alan,</p>
      <p class="para">Lorem Ipsum is simply dummy text of the printing and typesetting industry. Lorem Ipsum has been the industry's standard dummy text ever since the 1500s, when an unknown printer took a galley of type and scrambled it to make a type specimen book. It has survived not only five centuries, but also the leap into electronic typesetting, remaining essentially unchanged.</p>
      <p class="para">The standard chunk of Lorem Ipsum used since the 1500s is reproduced below for those interested. Sections 1.10.32 and 1.10.33 from "de Finibus Bonorum et Malorum" by Cicero are also reproduced in their exact original form, accompanied by English versions from the 1914 translation by H. Marlow.</p>
      <p class="para">Lorem Ipsum is simply dummy text of the printing and typesetting industry. Lorem Ipsum has been the industry's standard dummy text ever since the 1500s, when an unknown printer took a galley of type and scrambled it to make a type specimen book. It has survived not only five centuries, but also the leap into electronic typesetting, remaining essentially unchanged. It was popularised in the</p>
    </section>

    <section class="closing">
      <p>Sincerely Your,</p>
      <div class="signature" role="img" aria-label="Handwritten signature"></div>
      <p>Name Last Name<br>Company Name</p>
    </section>

    <address class="contact">
      <p>482 W. BROOK AVE. SUITE 214 PASADENA, CA 91847</p>
      <p><b>P</b> 626-555-0148 <b>E</b> info@quarn.com</p>
      <p>www.quarn.com</p>
    </address>

    <svg class="edge-lines" width="540" height="420" viewBox="0 0 540 420" aria-hidden="true">
      <polyline points="4,406 534,406 534,0" fill="none" stroke="var(--grey-light)" stroke-width="1"/>
      <rect x="0" y="410" width="540" height="10" fill="var(--blue-deep)"/>
      <rect x="0" y="410" width="540" height="3" fill="var(--blue-mid)"/>
    </svg>
  </article>
</body>
</html>
```